依頼詳細
1.渡航先の選択ページのデザイン
2.出発日の選択ページのデザイン
3.滞在期間の選択ページのデザイン
4.渡航目的の選択ページのデザイン
5.予約方法の選択ページのデザイン

流れが明確であれば、全て繋がった1ページ構成でも結構です

詳しくは添付資料を参照願います
ページ数
5ページ
希望イメージ
シンプル 複雑
単色 カラフル
暗い 明るい
日常 高級
遊び心 厳粛
未来的 伝統的
女性的 男性的
希望する色
青系、濃紺を主にした色合いでお願いいたします
納品ファイル
• 高解像度JPG (.jpg)
補足説明
スクリーンショットおよび、
サイトを構成するファイル一式をご納品いただきます
提案者制限を付加させいただきました
ファイル一式についての補足ですが、AIやPSD等の
画像を作成したツールでの保存形式ファイルもご納品のほどよろしくお願いいたします。
■ 選んだ理由

レベルの高いご提案を頂き、選定に悩みましたが、
「目指すコンセプトとの一致」と作り込み、質問を頂だいた事を鑑みて、選定とさせて頂きました。

■ 提案者全員のお礼・コメント

大変多くのご提案を頂き、どのデザインも甲乙付けがたいご提案で選定に悩みました。
今後また別の機会に、お力添えを頂ければ幸いです。
この度は誠にご提案ありがとうございました。

```html
<!DOCTYPE html>
<html lang="ja">
<head>
<meta charset="utf-8">
<title>海外渡航前ワクチン接種予約（新規）</title>
<link href="https://fonts.googleapis.com/css2?family=Noto+Sans+JP:wght@400;500;700&display=swap" rel="stylesheet">
<style>
:root{
  --navy:#0d3566;
  --navy-dark:#0a2b54;
  --step-idle:#b8c4d3;
  --text:#333333;
  --muted:#9a9a9a;
  --field:#ededed;
  --field-line:#cfcfcf;
  --map-land:#d9dadc;
  --map-sea:#ffffff;
  --stage:#eef0f3;
  --white:#ffffff;
}
*{box-sizing:border-box;margin:0;padding:0}
html,body{width:1200px;height:3664px;overflow:hidden;background:var(--stage);font-family:"Noto Sans JP",sans-serif;color:var(--text)}
.page{position:absolute;top:248px;left:0;width:1200px;height:3168px;background:var(--white)}
.site-header{position:absolute;top:0;left:0;width:1200px;height:160px;background:var(--navy);color:var(--white)}
.site-title{position:absolute;left:0;width:1100px;top:0;height:160px;line-height:160px;text-align:center;font-size:50px;font-weight:700;letter-spacing:1px}
.menu-icon{position:absolute;right:36px;top:52px}
.stepper{position:absolute;top:240px;left:0;width:1200px}
.step-line{position:absolute;top:34px;height:4px;background:var(--step-idle)}
.step{position:absolute;width:220px;margin-left:-110px;text-align:center}
.step-num{display:block;margin:0 auto;width:72px;height:72px;border-radius:50%;background:var(--step-idle);color:var(--white);font-size:38px;font-weight:700;line-height:72px}
.step-label{display:block;margin-top:28px;font-size:38px;line-height:48px;color:var(--muted)}
.step.is-active .step-num{background:var(--navy)}
.step.is-active .step-label{color:var(--text);font-weight:500}
.step-bar{position:absolute;top:584px;left:0;width:1200px;height:112px;border-top:6px solid var(--navy);border-bottom:6px solid var(--navy)}
.step-tag{position:absolute;left:0;top:-6px;width:300px;height:112px;background:var(--navy);color:var(--white);font-size:48px;font-weight:700;line-height:112px;text-align:center;letter-spacing:2px}
.step-title{position:absolute;left:300px;right:0;top:0;height:100px;line-height:100px;text-align:center;font-size:50px;font-weight:700;color:var(--navy)}
.lead{position:absolute;top:770px;left:0;width:1200px;text-align:center;font-size:42px;line-height:60px}
.section-heading{position:absolute;left:48px;font-size:46px;font-weight:700;color:var(--navy)}
.keyword-field{position:absolute;top:1008px;left:48px;width:1104px;height:128px;background:var(--field);border:2px solid var(--field-line);border-radius:6px;font-size:40px;line-height:124px;padding-left:40px;color:#b0b0b0}
.map{position:absolute;top:1328px;left:48px;width:1104px;height:760px;background:var(--map-sea);border:2px solid #e3e3e3}
.map-art{position:absolute;inset:0;background:linear-gradient(180deg,#e3e4e6 0%,var(--map-land) 60%,#e6e7e9 100%)}
.region{position:absolute;height:72px;background:var(--navy);color:var(--white);font-size:34px;font-weight:500;line-height:72px;padding-left:24px;border-radius:4px}
.region::after{content:"›";position:absolute;right:18px;top:-2px;font-size:44px}
.selected{position:absolute;top:2152px;left:48px;width:1104px;height:448px;background:var(--navy)}
.selected-title{position:absolute;top:40px;width:100%;text-align:center;color:var(--white);font-size:44px;font-weight:700}
.chip{position:absolute;height:100px;background:var(--white);font-size:40px;font-weight:500;line-height:100px;text-align:center;color:var(--text);padding-right:40px}
.chip-close{position:absolute;right:20px;top:0;color:#777;font-size:44px;font-weight:400}
.next-button{position:absolute;top:2700px;left:340px;width:520px;height:128px;background:var(--navy);color:var(--white);font-size:44px;font-weight:700;line-height:128px;text-align:center}
.next-button svg{position:absolute;right:40px;top:42px}
.site-footer{position:absolute;top:3028px;left:0;width:1200px;height:140px;background:var(--navy);color:var(--white);font-size:32px;font-weight:700;text-align:center;line-height:140px}
</style>
</head>
<body>
<main class="page">
  <header class="site-header">
    <h1 class="site-title">海外渡航前ワクチン接種予約（新規）</h1>
    <svg class="menu-icon" width="56" height="56" viewBox="0 0 56 56" aria-label="メニュー"><g stroke="#fff" stroke-width="5"><line x1="4" y1="8" x2="52" y2="8"/><line x1="4" y1="28" x2="52" y2="28"/><line x1="4" y1="48" x2="52" y2="48"/></g></svg>
  </header>

  <nav class="stepper">
    <div class="step-line" style="left:180px;width:840px"></div>
    <div class="step is-active" style="left:144px"><span class="step-num">1</span><span class="step-label">渡航先<br>選択</span></div>
    <div class="step" style="left:372px"><span class="step-num">2</span><span class="step-label">出発日<br>滞在期間<br>選択</span></div>
    <div class="step" style="left:600px"><span class="step-num">3</span><span class="step-label">渡航目的<br>予約方法<br>選択</span></div>
    <div class="step" style="left:824px"><span class="step-num">4</span><span class="step-label">ユーザー<br>情報入力</span></div>
    <div class="step" style="left:1052px"><span class="step-num">5</span><span class="step-label">予約完了</span></div>
  </nav>

  <div class="step-bar"><span class="step-tag">STEP 1</span><h2 class="step-title">渡航先選択</h2></div>

  <p class="lead">渡航先を選択してください。複数の選択が可能です。</p>

  <h3 class="section-heading" style="top:906px">キーワードから探す</h3>
  <div class="keyword-field">キーワードを入力してください</div>

  <h3 class="section-heading" style="top:1226px">地図から探す</h3>
  <div class="map">
    <div class="map-art" role="img" aria-label="地域を選べる世界地図"></div>
    <a class="region" style="left:40px;top:108px;width:256px">ヨーロッパ</a>
    <a class="region" style="left:324px;top:144px;width:256px">アジア</a>
    <a class="region" style="left:176px;top:256px;width:248px">中東</a>
    <a class="region" style="left:664px;top:224px;width:248px">北米</a>
    <a class="region" style="left:40px;top:400px;width:248px">アフリカ</a>
    <a class="region" style="left:524px;top:424px;width:256px">オセアニア</a>
    <a class="region" style="left:812px;top:460px;width:252px">南米</a>
  </div>

  <section class="selected">
    <h3 class="selected-title">選択した渡航先</h3>
    <div class="chip" style="left:52px;top:148px;width:492px">オセアニア<span class="chip-close">×</span></div>
    <div class="chip" style="left:576px;top:148px;width:476px">オーストラリア<span class="chip-close">×</span></div>
    <div class="chip" style="left:316px;top:300px;width:476px">グアム<span class="chip-close">×</span></div>
  </section>

  <a class="next-button">次へ<svg width="24" height="44" viewBox="0 0 24 44"><polyline points="4,4 20,22 4,40" fill="none" stroke="#fff" stroke-width="5"/></svg></a>

  <footer class="site-footer">Copyright © ●●●●●●●●●●. All Rights Reserved.</footer>
</main>
</body>
</html>
```